Build us a LinkedIn Banner

We are a small fintech with a big mission, visit Vantoro.io. As part of our corporate identity we need consistent LinkedIn banner across all employees. The project is design of such LinkedIn banner. Besides looking cool (still sincere and serious), there should be a quote:

we BUIDL the future

Please note "BUIDL" which is intentionally spelt that way.
Please also no portrait pictures of the founders.
The size of LinkedIn banner: 1584 x 396 pixels (optimal dimensions), 8 MB maximum.

The best proposal will be awarded.

```html
<!DOCTYPE html>
<html lang="en">
<head>
<meta charset="utf-8">
<title>Vantoro LinkedIn Banner</title>
<link rel="stylesheet" href="https://fonts.googleapis.com/css2?family=Source+Sans+3:wght@400&display=swap">
<style>
  :root {
    --page: #ffffff;
    --night-top: #0b1d3a;
    --night-mid: #112a4d;
    --night-low: #1a3458;
    --glow: #3b4a5e;
    --quote: #3ba4e6;
    --brand: #8ea7c8;
  }
  html, body {
    margin: 0;
    width: 1200px;
    height: 1060px;
    overflow: hidden;
    background: var(--page);
  }
  .canvas {
    position: relative;
    width: 1200px;
    height: 1060px;
  }
  .banner {
    position: absolute;
    left: 67px;
    top: 403px;
    width: 1016px;
    height: 253px;
    display: block;
  }
  .quote-text {
    font-family: "Source Sans 3", "Myriad Pro", sans-serif;
    fill: var(--quote);
    font-weight: 400;
  }
  .brand-name {
    font-family: "Source Sans 3", "Myriad Pro", sans-serif;
    fill: var(--brand);
    font-weight: 400;
    letter-spacing: 0.5px;
  }
</style>
</head>
<body>
<main class="canvas">
  <svg class="banner" viewBox="0 0 1016 253" xmlns="http://www.w3.org/2000/svg">
    <defs>
      <linearGradient id="night-sky" x1="0" y1="0" x2="0" y2="1">
        <stop offset="0" stop-color="var(--night-top)"/>
        <stop offset="0.45" stop-color="var(--night-mid)"/>
        <stop offset="1" stop-color="var(--night-low)"/>
      </linearGradient>
      <radialGradient id="city-glow" cx="0.45" cy="0.85" r="0.6">
        <stop offset="0" stop-color="var(--glow)" stop-opacity="0.55"/>
        <stop offset="1" stop-color="var(--glow)" stop-opacity="0"/>
      </radialGradient>
    </defs>

    <g class="skyline-photo" role="img" aria-label="Night-time city skyline with illuminated towers">
      <rect width="1016" height="253" fill="url(#night-sky)"/>
      <rect width="1016" height="253" fill="url(#city-glow)"/>
    </g>

    <g class="brand">
      <circle cx="34" cy="20" r="9" fill="none" stroke="var(--brand)" stroke-width="1.5"/>
      <text class="brand-name" x="7" y="59" font-size="26">VANTORO</text>
    </g>

    <g class="quote">
      <text class="quote-text" x="276" y="71" font-size="50">We</text>
      <text class="quote-text" x="298" y="144" font-size="102">BUIDL</text>
      <text class="quote-text" x="368" y="200" font-size="44">the</text>
      <text class="quote-text" x="441" y="220" font-size="94">FUTURE</text>
    </g>
  </svg>
</main>
</body>
</html>
```